TALLIS AT DWELLINGS, LLC Webpage portfolio

I want to create a Website that allows my potential clients to browse my Skilled work via before and after photos. I want the website to enhance the work that I provide and potentially drive new business, or at least solidify my work.
I also do 3D CAD and Modeling of New Spaces and it would be nice to show some of that work from pencil design to 3D modeling, which I feel may help give me more clients.

The website needs to show a solid carpenter/company with the skills to get any project completed.

Types of Jobs - Custom Carpentry & Finishes, Kitchens, Baths, Basements, Decks, Porches, Whole House Renovation - Skilled Craftsmanship (Hardwood Flooring, Floor and Wall Tile) and much more...

Target Market(s)

Residential Home Renovation, Kitchen and Bath Renovation, Home Improvement

Industry/Entity Type

Residential Construction

Number of Pages Required

5+ page

Font styles to use
Sans Serif
Script

Requirements
Must have
• Similar to Rimvale.com, except for Tallis At Dwellings.
• Must be inviting.
• My Services Offered
• A way to reach me or contact me for estimates with some sort of Screening Questionare.
Nice to have
• Inviting Colors
Should not have
• Not sure at this time

```html
<!DOCTYPE html>
<html lang="en">
<head>
<meta charset="utf-8">
<title>Tallis At Dwellings — Home Renovation &amp; Carpentry</title>
<link href="https://fonts.googleapis.com/css2?family=Open+Sans:ital,wght@0,400;0,600;0,700;0,800;1,400&display=swap" rel="stylesheet">
<style>
:root{
  --blue:#2a9fd8;
  --navy:#1d3e5e;
  --ink:#222;
  --text:#666;
  --muted:#999;
  --line:#e3e3e3;
  --footer:#2b2b2b;
  --footer-deep:#1f1f1f;
  --footer-text:#b5b5b5;
  --white:#fff;
}
*{margin:0;padding:0;box-sizing:border-box}
html,body{width:1200px;height:3922px;overflow:hidden}
body{font-family:"Open Sans",Arial,sans-serif;color:var(--text);background:var(--white);position:relative}
.abs{position:absolute}
a{color:inherit;text-decoration:none}

/* header */
.site-header{left:0;top:0;width:1200px;height:84px;background:var(--white)}
.brand{left:66px;top:22px;display:flex;align-items:center;gap:10px}
.brand-mark{width:30px;height:30px;background:var(--navy)}
.brand-name{font-size:18px;font-weight:700;color:var(--navy)}
.main-nav{left:370px;top:34px;display:flex;gap:0}
.main-nav a{font-size:13px;color:#444;text-transform:uppercase;letter-spacing:.3px;margin-right:52px}
.login{left:1046px;top:26px;width:84px;height:32px;border:1px solid var(--blue);color:var(--blue);font-size:12px;text-align:center;line-height:30px;text-transform:uppercase}

/* hero */
.hero{left:0;top:84px;width:1200px;height:575px;background:linear-gradient(135deg,#3a2414 0%,#6b3f22 35%,#4a2b17 60%,#7a5638 85%,#2e1c10 100%)}
.hero-shade{left:0;top:84px;width:1200px;height:575px;background:rgba(0,0,0,.25)}
.hero-title{left:0;top:300px;width:1200px;text-align:center;color:var(--white);font-size:40px;font-weight:700;letter-spacing:1px}
.hero-sub{left:0;top:340px;width:1200px;text-align:center;color:var(--white);font-size:29px;font-weight:400;letter-spacing:4px;text-transform:uppercase}
.hero-btn{left:491px;top:403px;width:217px;height:41px;border:1px solid var(--white);color:var(--white);font-size:12px;text-align:center;line-height:39px;text-transform:uppercase}

/* welcome */
.section-title{left:0;width:1200px;text-align:center;color:var(--ink);font-size:32px;font-weight:700;text-transform:uppercase}
.intro{left:196px;top:780px;width:810px;text-align:center;font-size:13px;line-height:26px}
.service{width:300px;text-align:center}
.service-icon{width:82px;height:82px;border-radius:50%;background:var(--blue);margin:0 auto;display:flex;align-items:center;justify-content:center}
.service-name{margin-top:42px;font-size:15px;font-weight:700;color:var(--ink);text-transform:uppercase}
.service-text{margin-top:10px;font-size:12.5px;line-height:26px;padding:0 8px}
.carousel-arrow{top:1016px}

/* works */
.block-heading{font-size:15px;font-weight:700;color:var(--navy);text-transform:uppercase}
.outline-btn{width:143px;height:39px;border:1px solid var(--blue);color:var(--blue);font-size:12.5px;text-align:center;line-height:37px}
.work-photo{width:319px;height:220px}
.work-title{font-size:13px;color:var(--ink);font-weight:600}
.work-sub{font-size:11px;color:var(--muted);padding-bottom:8px;border-bottom:1px solid var(--line);width:319px}

/* how it works */
.how{left:99px;top:1913px;width:1001px;height:380px;background:linear-gradient(90deg,#f4f4f4 0%,#ececec 50%,#dcdfe2 100%)}
.how-art{left:560px;top:1925px;width:520px;height:360px;background:linear-gradient(160deg,#e9ecef 0%,#cfd6dc 55%,#9fb48a 100%)}
.how-title{left:173px;top:2008px;font-size:44px;font-weight:800;color:var(--navy);text-transform:uppercase}
.how-text{left:173px;top:2072px;width:400px;font-size:18px;line-height:27px;color:var(--blue)}
.fill-btn{background:var(--blue);color:var(--white);font-weight:600;text-align:center;text-transform:uppercase}

/* about */
.about{left:0;top:2755px;width:1200px;height:437px;background:linear-gradient(100deg,#3e3a36 0%,#6d6156 40%,#8a7c6e 60%,#3a3632 100%)}
.about-shade{left:0;top:2755px;width:1200px;height:437px;background:rgba(20,20,20,.45)}
.about-kicker{left:0;top:2822px;width:1200px;text-align:center;color:var(--white);font-size:24px;font-weight:700;text-transform:uppercase}
.about-title{left:0;top:2852px;width:1200px;text-align:center;color:var(--white);font-size:46px;font-weight:800;text-transform:uppercase}
.about-sub{left:0;top:2922px;width:1200px;text-align:center;color:#eee;font-size:15px;text-transform:uppercase}
.about-text{left:170px;top:2958px;width:860px;text-align:center;color:#eee;font-size:13px;line-height:26px}

/* testimonial */
.testi-title{left:0;top:3258px;width:1200px;text-align:center;font-size:26px;font-weight:700;color:var(--navy);text-transform:uppercase}
.avatar{left:160px;top:3320px;width:188px;height:188px;border-radius:50%;background:radial-gradient(circle at 50% 40%,#d9c0a8 0%,#b59476 55%,#8a8f95 100%)}
.quote-mark{font-size:60px;color:#ccc;font-style:italic;line-height:1}
.quote-text{left:450px;top:3358px;width:560px;font-size:13px;line-height:26px;font-style:italic;color:var(--muted)}
.quote-name{left:450px;top:3456px;font-size:15px;color:var(--blue);font-weight:600}
.quote-role{left:450px;top:3480px;font-size:12px;color:var(--ink)}
.dot{width:11px;height:11px;border-radius:50%;border:1px solid #aaa}

/* footer */
.footer{left:0;top:3594px;width:1200px;height:262px;background:var(--footer)}
.footer-col h4{font-size:14px;font-weight:700;color:var(--white);text-transform:uppercase;margin-bottom:14px}
.footer-col p,.footer-col li{font-size:12px;line-height:26px;color:var(--footer-text);list-style:none}
.footer-more{color:var(--white)!important;margin-top:8px}
.footer-bar{left:0;top:3856px;width:1200px;height:66px;background:var(--footer-deep)}
.copyright{left:99px;top:3880px;font-size:11.5px;color:var(--footer-text)}
.social{left:772px;top:3880px;font-size:11.5px;color:var(--footer-text);display:flex;align-items:center;gap:22px}
.social i{display:block;width:12px;height:12px;border-radius:50%;background:#777}
</style>
</head>
<body>

<header class="abs site-header">
  <div class="abs brand"><span class="brand-mark"></span><span class="brand-name">Tallis At Dwellings</span></div>
  <nav class="abs main-nav">
    <a href="#">Home</a><a href="#">About Us</a><a href="#">Services</a><a href="#">Works</a><a href="#">Before &amp; After</a><a href="#">Testimonials</a>
  </nav>
  <a class="abs login" href="#">Login</a>
</header>

<section>
  <div class="abs hero" role="img" aria-label="Warm-lit kitchen interior with dark wood cabinets, pendant lamps and bar stools"></div>
  <div class="abs hero-shade"></div>
  <h1 class="abs hero-title">TALLIS AT DWELLINGS</h1>
  <p class="abs hero-sub">I also do 3D CAD and modeling of new spaces</p>
  <a class="abs hero-btn" href="#">Click here for view details</a>
</section>

<section>
  <h2 class="abs section-title" style="top:733px">Welcome to Tallis At Dwellings</h2>
  <p class="abs intro">Lorem Ipsum is simply dummy text of the printing and typesetting industry. Lorem Ipsum has been the industry's standard dummy text ever since the 1500s, when an unknown printer took a galley of type and scrambled it to make a type specimen book. It has survived not only five centuries, but also the leap into electronic typesetting</p>

  <svg class="abs carousel-arrow" style="left:62px" width="16" height="26" viewBox="0 0 16 26"><path d="M13 2 3 13l10 11" fill="none" stroke="#bbb" stroke-width="2"/></svg>
  <svg class="abs carousel-arrow" style="left:1122px" width="16" height="26" viewBox="0 0 16 26"><path d="M3 2l10 11L3 24" fill="none" stroke="#bbb" stroke-width="2"/></svg>

  <div class="abs service" style="left:106px;top:920px">
    <div class="service-icon"><svg width="40" height="40" viewBox="0 0 40 40"><path d="M6 26 28 8l6 6-22 18z" fill="none" stroke="#fff" stroke-width="2.5"/><path d="M10 23l6 6" stroke="#fff" stroke-width="2.5"/></svg></div>
    <div class="service-name">Custom Carpentry &amp; Finishes</div>
    <p class="service-text">Lorem Ipsum is simply dummy text of the printing and typesetting industry. Lorem Ipsum has been the industry's standard</p>
  </div>
  <div class="abs service" style="left:449px;top:920px">
    <div class="service-icon"><svg width="40" height="40" viewBox="0 0 40 40"><rect x="9" y="7" width="22" height="27" rx="2" fill="none" stroke="#fff" stroke-width="2.5"/><path d="M9 15h22" stroke="#fff" stroke-width="2.5"/><circle cx="14" cy="11" r="1.5" fill="#fff"/><circle cx="19" cy="11" r="1.5" fill="#fff"/><rect x="14" y="20" width="12" height="9" fill="none" stroke="#fff" stroke-width="2"/></svg></div>
    <div class="service-name">Kitchens</div>
    <p class="service-text">Lorem Ipsum is simply dummy text of the printing and typesetting industry. Lorem Ipsum has been the industry's standard</p>
  </div>
  <div class="abs service" style="left:791px;top:920px">
    <div class="service-icon"><svg width="40" height="40" viewBox="0 0 40 40"><path d="M6 20h28v4a8 8 0 0 1-8 8H14a8 8 0 0 1-8-8z" fill="none" stroke="#fff" stroke-width="2.5"/><path d="M10 20V10a3 3 0 0 1 6 0" fill="none" stroke="#fff" stroke-width="2.5"/><path d="M12 32l-2 4M28 32l2 4" stroke="#fff" stroke-width="2.5"/></svg></div>
    <div class="service-name">Baths</div>
    <p class="service-text">Lorem Ipsum is simply dummy text of the printing and typesetting industry. Lorem Ipsum has been the industry's standard</p>
  </div>
</section>

<section>
  <h3 class="abs block-heading" style="left:99px;top:1226px">Newest Works &raquo;</h3>
  <a class="abs outline-btn" style="left:957px;top:1218px" href="#">View more works</a>

  <div class="abs work-photo" style="left:99px;top:1278px;background:linear-gradient(135deg,#5a3a22,#a57650 60%,#3b2818)" role="img" aria-label="Kitchen with granite island and pendant lights"></div>
  <div class="abs work-photo" style="left:442px;top:1278px;background:linear-gradient(160deg,#cfd3d6,#9d8f80 60%,#5b4b3c)" role="img" aria-label="White porch with railing and stone column"></div>
  <div class="abs work-photo" style="left:784px;top:1278px;background:linear-gradient(140deg,#d9b78a,#b07a4a 55%,#6a5a40)" role="img" aria-label="Portfolio feature photo"></div>

  <div class="abs" style="left:99px;top:1512px"><div class="work-title">Lorem Ipsum is simply</div><div class="work-sub">Lorem ipsum is simply dummy text...</div></div>
  <div class="abs" style="left:442px;top:1512px"><div class="work-title">Lorem Ipsum is simply</div><div class="work-sub">Lorem ipsum is simply dummy text...</div></div>
  <div class="abs" style="left:784px;top:1512px"><div class="work-title">Lorem Ipsum is simply</div><div class="work-sub">Lorem ipsum is simply dummy text...</div></div>

  <div class="abs work-photo" style="left:99px;top:1581px;background:linear-gradient(135deg,#2e2118,#7a4e30 55%,#c08a5c)" role="img" aria-label="Dining room with hardwood floor"></div>
  <div class="abs work-photo" style="left:442px;top:1581px;background:linear-gradient(135deg,#6e3a20,#b86a3c 50%,#4a2a18)" role="img" aria-label="Renovated kitchen with island"></div>
  <div class="abs work-photo" style="left:784px;top:1581px;background:linear-gradient(160deg,#e2e4e6,#a6a09a 55%,#6b6259)" role="img" aria-label="House exterior with covered porch and stairs"></div>

  <div class="abs" style="left:99px;top:1815px"><div class="work-title">Lorem Ipsum is simply</div><div class="work-sub">Lorem ipsum is simply dummy text...</div></div>
  <div class="abs" style="left:442px;top:1815px"><div class="work-title">Lorem Ipsum is simply</div><div class="work-sub">Lorem ipsum is simply dummy text...</div></div>
  <div class="abs" style="left:784px;top:1815px"><div class="work-title">Lorem Ipsum is simply</div><div class="work-sub">Lorem ipsum is simply dummy text...</div></div>
</section>

<section>
  <div class="abs how"></div>
  <div class="abs how-art" role="img" aria-label="Pencil sketch of a modern house turning into a 3D rendering"></div>
  <h2 class="abs how-title">How it works</h2>
  <p class="abs how-text">Lorem Ipsum is simply dummy text of the printing and typesetting industry.</p>
  <a class="abs fill-btn" style="left:173px;top:2149px;width:167px;height:52px;line-height:52px;font-size:15px" href="#">View Design</a>
</section>

<section>
  <h3 class="abs block-heading" style="left:99px;top:2348px">Before &amp; After Works &raquo;</h3>
  <a class="abs outline-btn" style="left:963px;top:2338px;width:137px" href="#">View more Works</a>

  <div class="abs work-photo" style="left:99px;top:2400px;background:linear-gradient(90deg,#8a6a4c 0 50%,#6b3c22 50%)" role="img" aria-label="Before and after of a kitchen remodel"></div>
  <div class="abs work-photo" style="left:442px;top:2400px;background:linear-gradient(90deg,#9c8a74 0 50%,#5a3420 50%)" role="img" aria-label="Before and after of a gutted room made into a kitchen"></div>
  <div class="abs work-photo" style="left:784px;top:2400px;background:linear-gradient(90deg,#b4a89a 0 50%,#6e3a22 50%)" role="img" aria-label="Before and after of an interior renovation"></div>

  <div class="abs" style="left:99px;top:2634px"><div class="work-title">Lorem Ipsum is simply</div><div class="work-sub">Lorem ipsum is simply dummy text...</div></div>
  <div class="abs" style="left:442px;top:2634px"><div class="work-title">Lorem Ipsum is simply</div><div class="work-sub">Lorem ipsum is simply dummy text...</div></div>
  <div class="abs" style="left:784px;top:2634px"><div class="work-title">Lorem Ipsum is simply</div><div class="work-sub">Lorem ipsum is simply dummy text...</div></div>
</section>

<section>
  <div class="abs about" role="img" aria-label="Homeowner browsing on a laptop in a living room"></div>
  <div class="abs about-shade"></div>
  <div class="abs about-kicker">About</div>
  <h2 class="abs about-title">Tallis At Dwellings</h2>
  <p class="abs about-sub">Lorem Ipsum is simply dummy text of the printing and typesetting industry</p>
  <p class="abs about-text">Lorem Ipsum is simply dummy text of the printing and typesetting industry. Lorem Ipsum has been the industry's standard dummy text ever since the 1500s, when an unknown printer took a galley of type and scrambled it to make a type specimen book. It has survived not only five centuries, but also the leap into electronic typesetting, remaining essentially unchanged.</p>
  <a class="abs fill-btn" style="left:518px;top:3069px;width:167px;height:42px;line-height:42px;font-size:12.5px" href="#">View More Info</a>
</section>

<section>
  <h2 class="abs testi-title">What our client's say</h2>
  <div class="abs avatar" role="img" aria-label="Portrait of a smiling client"></div>
  <span class="abs quote-mark" style="left:416px;top:3340px">&ldquo;</span>
  <p class="abs quote-text">Lorem Ipsum is simply dummy text of the printing and typesetting industry. Lorem Ipsum has been the industry's standard dummy text ever since the 1500s, when an unknown printer took a galley of type and scrambled it to make a type specimen book...</p>
  <span class="abs quote-mark" style="left:1020px;top:3404px">&rdquo;</span>
  <div class="abs quote-name">Marlon Keswick</div>
  <div class="abs quote-role">Business man</div>
  <span class="abs dot" style="left:1010px;top:3482px;background:#aaa"></span>
  <span class="abs dot" style="left:1026px;top:3482px"></span>
</section>

<footer>
  <div class="abs footer"></div>
  <div class="abs footer-col" style="left:99px;top:3630px;width:330px">
    <h4>Who we are?</h4>
    <p>Lorem Ipsum is simply dummy text of the printing and typesetting industry. Lorem Ipsum has been the industry's standard dummy text ever since the 1500s, when an unknown printer took a galley of type and scrambled it...</p>
    <p class="footer-more">Read more info &nbsp;&rsaquo;</p>
  </div>
  <div class="abs footer-col" style="left:541px;top:3630px">
    <h4>Welcome</h4>
    <ul><li>Home</li><li>About Us</li><li>Services</li><li>Works</li><li>Before &amp; After</li><li>Testimonials</li></ul>
  </div>
  <div class="abs footer-col" style="left:740px;top:3630px">
    <h4>Information</h4>
    <ul><li>Terms &amp; Conditions</li><li>Privacy Policy</li><li>Contact Us</li><li>Disclaimer</li><li>Sitemap</li></ul>
  </div>
  <div class="abs footer-col" style="left:933px;top:3630px;width:230px">
    <h4>Contact Info</h4>
    <p>48 Alder Lane, Brookfield,<br>Country name - 965220</p>
    <p style="margin-top:6px">&#9990;&nbsp; (555) 014-2290</p>
    <p>&#9993;&nbsp; info@tallisatdwellings.com</p>
  </div>
  <div class="abs footer-bar"></div>
  <p class="abs copyright">&copy; 2017. Tallis At Dwellings. All rights reserved.</p>
  <div class="abs social">Connect with our social network : <i></i><i></i><i></i><i></i><i></i></div>
</footer>

</body>
</html>
```